Awesome photographers card for an awesome new business

Double sided business card Black background and silver logo in middle on one side. Details on otherside. please keep it simple

Photographer

Gavin Tolley
0482615073
GavinTolleyPhotography82@lumenpost.com
www.GavinTolleyPhotography.com.au
Instagram _Gavin_tolley

Requirements
Must have
• My logo in Silver
• please use instagram logo instead of "Instagram"

```html
<!DOCTYPE html>
<html lang="en">
<head>
<meta charset="utf-8">
<title>Gavin Tolley Photography – Business Card</title>
<link href="https://fonts.googleapis.com/css2?family=Montserrat:wght@300;500;600&display=swap" rel="stylesheet">
<style>
  :root {
    --backdrop: #ececed;
    --card: #1c1c1c;
    --card-edge: #262626;
    --ink: #f4f4f4;
    --silver: #c8c8ca;
    --accent: #d3262e;
  }
  * { box-sizing: border-box; margin: 0; padding: 0; }
  html, body {
    width: 1200px; height: 1200px; overflow: hidden;
    background: var(--backdrop);
    font-family: "Montserrat", sans-serif;
  }
  .sheet {
    width: 1200px; height: 1200px;
    display: flex; flex-direction: column;
    align-items: center; justify-content: center;
    gap: 80px;
  }
  .card {
    width: 700px; height: 400px;
    background: linear-gradient(135deg, var(--card) 0%, var(--card-edge) 100%);
    border-radius: 4px;
    box-shadow: 0 18px 40px rgba(0,0,0,0.18);
    position: relative;
  }
  /* Front: brand mark */
  .card--front {
    display: flex; align-items: center; justify-content: center;
  }
  .brand {
    display: flex; align-items: center; gap: 22px;
  }
  .brand__dot {
    width: 56px; height: 56px; border-radius: 50%;
    border: 3px solid var(--silver);
  }
  .brand__name {
    color: var(--silver);
    font-weight: 500;
    font-size: 26px;
    letter-spacing: 6px;
    text-transform: uppercase;
    line-height: 1.4;
  }
  /* Back: contact details */
  .card--back {
    padding: 70px 0 0 70px;
  }
  .holder {
    color: var(--ink);
    font-weight: 300;
    font-size: 34px;
    letter-spacing: 1px;
    text-transform: uppercase;
  }
  .rule {
    width: 70px; height: 3px;
    background: var(--accent);
    margin: 14px 0 22px;
  }
  .contacts { list-style: none; }
  .contact {
    display: flex; align-items: center; gap: 14px;
    color: var(--ink);
    font-weight: 600;
    font-size: 18px;
    line-height: 1.75;
  }
  .contact__icon { width: 18px; height: 18px; flex: none; }
  .rule--short { width: 60px; margin: 10px 0 12px; }
  .website {
    color: var(--ink);
    font-weight: 600;
    font-size: 18px;
  }
</style>
</head>
<body>
<main class="sheet">

  <section class="card card--front" aria-label="Card front">
    <div class="brand">
      <span class="brand__dot"></span>
      <span class="brand__name">Gavin Tolley<br>Photography</span>
    </div>
  </section>

  <section class="card card--back" aria-label="Card back">
    <h1 class="holder">Gavin Tolley</h1>
    <div class="rule"></div>
    <ul class="contacts">
      <li class="contact">
        <svg class="contact__icon" viewBox="0 0 24 24" aria-hidden="true">
          <path fill="#f4f4f4" d="M6.6 10.8c1.4 2.8 3.8 5.1 6.6 6.6l2.2-2.2c.3-.3.7-.4 1-.2 1.1.4 2.3.6 3.6.6.6 0 1 .4 1 1V20c0 .6-.4 1-1 1C10.6 21 3 13.4 3 4c0-.6.4-1 1-1h3.5c.6 0 1 .4 1 1 0 1.3.2 2.5.6 3.6.1.3 0 .7-.2 1z"/>
        </svg>
        <span>0482615073</span>
      </li>
      <li class="contact">
        <svg class="contact__icon" viewBox="0 0 24 24" aria-hidden="true">
          <text x="12" y="18" text-anchor="middle" fill="#f4f4f4" font-family="Montserrat, sans-serif" font-weight="600" font-size="20">@</text>
        </svg>
        <span>GavinTolleyPhotography82@lumenpost.com</span>
      </li>
      <li class="contact">
        <svg class="contact__icon" viewBox="0 0 24 24" aria-hidden="true">
          <circle cx="12" cy="12" r="9" fill="none" stroke="#f4f4f4" stroke-width="2"/>
        </svg>
        <span>_Gavin_tolley</span>
      </li>
    </ul>
    <div class="rule rule--short"></div>
    <p class="website">www.GavinTolleyPhotography.com.au</p>
  </section>

</main>
</body>
</html>
```